Moxtrel Compensation Lawyers

We need a modern, sleek letterhead that is professional.

In relation to the footer, we would like to have firm contact details there ideally, however you must also insert at the bottom of each page the following....

Liability limited by a scheme approved under the Professional Standards Legislation.

From the attachment you can extract the firm logo. Also, I would like the Accredited specialist circle on the letterhead also.

Also, I would like you to create a document that can easily be edited for change of contact details, as these are likely to change.

Industry/Entity Type

It Professional

Font styles to use
Sans Serif

Colors
0655a3
3276b5
85abd2
0492cd
33a6d7
85cae6
cee9f5
eaf1f7
cbcbcb

Requirements
Must have
• Ph: 9317-2856
• F: 9184-3720
• M 0435-618-294
• kp@moxtrel.com.au
• www.moxtrel.com.au
Nice to have
• the word document gives you an idea of what I like. I am happy for your to amaze me with your creativity.

```html
<!DOCTYPE html>
<html lang="en">
<head>
<meta charset="utf-8">
<title>Moxtrel Compensation Lawyers – Letterhead</title>
<link rel="stylesheet" href="https://fonts.googleapis.com/css2?family=Source+Sans+3:wght@400;600&display=swap">
<style>
  :root {
    --navy: #0655a3;
    --azure: #33a6d7;
    --sky: #85cae6;
    --mist: #eaf1f7;
    --ice: #cee9f5;
    --ink: #5a5a5a;
    --muted: #8a8a8a;
    --backdrop: #e4e6e9;
    --paper: #ffffff;
  }
  * { box-sizing: border-box; margin: 0; padding: 0; }
  html, body {
    width: 1145px;
    height: 1200px;
    overflow: hidden;
    background: var(--backdrop);
    font-family: "Source Sans 3", "Myriad Pro", Arial, sans-serif;
  }
  .letterhead {
    position: absolute;
    left: 162px;
    top: 20px;
    width: 820px;
    height: 1160px;
    background: var(--paper);
    overflow: hidden;
  }
  .brand {
    position: absolute;
    left: 28px;
    top: 30px;
    display: flex;
    align-items: center;
    gap: 20px;
  }
  .brand-dot {
    width: 66px;
    height: 66px;
    border-radius: 50%;
    background: var(--azure);
    flex: none;
  }
  .brand-name {
    font-size: 28px;
    font-weight: 400;
    color: var(--navy);
    line-height: 1;
    letter-spacing: -0.2px;
  }
  .brand-web {
    margin-top: 6px;
    font-size: 15px;
    color: var(--azure);
    letter-spacing: 1.2px;
    line-height: 1;
  }
  .contact {
    position: absolute;
    right: 31px;
    top: 34px;
    text-align: right;
    font-size: 12px;
    line-height: 15.5px;
    color: var(--ink);
    list-style: none;
  }
  .watermark {
    position: absolute;
    left: 126px;
    top: 342px;
    width: 566px;
    height: 413px;
    background: radial-gradient(ellipse at 50% 55%, var(--ice) 0%, var(--mist) 45%, rgba(234,241,247,0) 72%);
    opacity: 0.8;
  }
  .footer {
    position: absolute;
    left: 0;
    right: 0;
    bottom: 0;
    text-align: center;
  }
  .accreditation {
    width: 58px;
    height: 58px;
    margin: 0 auto 14px;
    border-radius: 50%;
    border: 2px solid var(--sky);
    background: var(--mist);
  }
  .practice-areas {
    font-size: 16px;
    color: var(--navy);
    letter-spacing: 0.2px;
    line-height: 1;
  }
  .practice-areas .sep { margin: 0 6px; }
  .disclaimer {
    margin-top: 5px;
    font-size: 10.5px;
    color: var(--muted);
    line-height: 1;
  }
  .footer-band {
    margin-top: 16px;
    height: 19px;
    background: var(--azure);
  }
</style>
</head>
<body>
  <main class="letterhead">
    <header class="brand">
      <span class="brand-dot" aria-hidden="true"></span>
      <div class="brand-text">
        <h1 class="brand-name">Moxtrel Compensation Lawyers</h1>
        <p class="brand-web">www.moxtrel.com.au</p>
      </div>
    </header>

    <ul class="contact">
      <li>Ph: 9317-2856</li>
      <li>F: 9184-3720</li>
      <li>M 0435-618-294</li>
      <li>kp@moxtrel.com.au</li>
    </ul>

    <div class="watermark" role="img" aria-label="Faint decorative brand watermark area"></div>

    <footer class="footer">
      <div class="accreditation" role="img" aria-label="Accredited specialist badge"></div>
      <p class="practice-areas">INSURANCE LAW<span class="sep">|</span>ESTATE &amp; PROPERTY LAW<span class="sep">|</span>FAMILY LAW<span class="sep">|</span>COMMERCIAL LAW</p>
      <p class="disclaimer">Liability limited by a scheme approved under the Professional Standards Legislation.</p>
      <div class="footer-band"></div>
    </footer>
  </main>
</body>
</html>
```